Redone of Site on Wix

Project Overview: Website Redesign for Brovento
We are looking to redesign our current website, www.broventousa.com, to better match the style and functionality of these reference sites:
Quorine Health
ZRM FlexTap
Key Requirements: Modern, Clean Design:
The site should have a professional and clean layout with clear messaging about our services.
Visual Elements: Use strong visuals like images, icons, or illustrations to support text and engage visitors.
Clear Service Breakdown: Easily digestible sections explaining what Brovento offers, similar to the service explanations on the reference sites.
User-Friendly Navigation: Simple, intuitive navigation with visible CTAs (e.g., "Learn More," "Get Started").
Trust-Building Features: Incorporate trust elements like client logos, testimonials, or success stories to build credibility.
Mobile-Responsive:
Ensure the website is fully responsive and looks great on all devices (desktop, tablet, mobile).
SEO Optimization:
Deliverables: Fully functional website with modern design.
All content will be provided, but we may need help with imagery or layout recommendations.
Responsive design and mobile optimization.
We are looking for a clean, modern, and easy-to-navigate site that reflects the professionalism of our brand.

```html
<!DOCTYPE html>
<html lang="en">
<head>
<meta charset="utf-8">
<title>Brovento – Essential Nutrition For Better Living</title>
<link href="https://fonts.googleapis.com/css2?family=Oswald:wght@300;400&family=Montserrat:ital,wght@0,400;0,500;0,600;0,700;1,400&display=swap" rel="stylesheet">
<style>
:root{
  --red:#b92b2e;
  --red-dark:#a72225;
  --ink:#1d1d1f;
  --muted:#5a5a5a;
  --soft:#f3f3f3;
  --line:#e4e4e4;
  --gold:#f2b418;
  --white:#fff;
}
*{box-sizing:border-box;margin:0;padding:0}
html,body{width:1200px;height:5004px;overflow:hidden;background:var(--white)}
body{font-family:"Montserrat",sans-serif;color:var(--ink);position:relative}
section,header,footer{position:absolute;left:0;width:1200px}
.abs{position:absolute}
.display{font-family:"Oswald",sans-serif;font-weight:300;letter-spacing:.5px}
.btn{position:absolute;display:flex;align-items:center;justify-content:center;gap:8px;border-radius:30px;font-weight:600;font-size:17px;text-transform:uppercase}
.btn-outline{border:2px solid var(--red);color:var(--red);background:var(--white)}
.btn-solid{background:var(--red);color:var(--white)}
.arrow{width:16px;height:16px}

/* header */
.site-header{top:0;height:113px;background:var(--white)}
.brand{position:absolute;font-family:"Montserrat",sans-serif;font-weight:500;color:var(--red)}
.site-header .brand{left:64px;top:22px;font-size:46px}
.nav{position:absolute;top:68px;left:355px;display:flex;gap:48px;font-size:15px;color:#333}
.tab-cta{position:absolute;left:909px;top:0;width:233px;height:40px;background:var(--red);color:#fff;font-weight:600;font-size:16px;display:flex;align-items:center;justify-content:center;gap:8px;clip-path:polygon(0 0,100% 0,94% 100%,6% 100%)}

/* hero */
.hero{top:113px;height:592px;background:linear-gradient(90deg,#f5f3f1 0%,#f1ece7 42%,#e7d3bf 62%,#c98f6a 80%,#e8e0d6 100%)}
.hero h1{position:absolute;left:124px;top:112px;font-size:60px;line-height:66px;color:#222}
.hero p{position:absolute;left:126px;top:280px;width:360px;font-size:18px;line-height:25px;font-weight:500}
.hero .btn{left:127px;top:387px;width:160px;height:56px;font-size:15px}

/* offers */
.offers{top:705px;height:730px;background:linear-gradient(180deg,#fff 0%,#fbf3f3 60%,#fff 100%)}
.section-title{position:absolute;left:0;width:1200px;text-align:center;font-size:54px;color:#222}
.offer-card{position:absolute;top:198px;width:296px;height:351px;background:#fff;border-radius:12px;box-shadow:0 6px 22px rgba(0,0,0,.07);padding:20px 32px}
.offer-icon{width:100px;height:100px;border-radius:50%;background:var(--red);display:flex;align-items:center;justify-content:center}
.offer-card h3{margin-top:14px;font-weight:400;font-size:26px;line-height:30px;color:#333}
.offer-card p{margin-top:18px;font-size:13.5px;line-height:19px;color:var(--muted)}
.offer-card .more{position:absolute;left:32px;bottom:24px;font-size:13px;font-weight:600;display:flex;align-items:center;gap:8px}

/* product */
.product{top:1435px;height:736px}
.product .sub{position:absolute;left:0;width:1200px;top:155px;text-align:center;font-size:21px;font-weight:600;color:#333;line-height:27px}
.product-copy{position:absolute;left:641px;top:318px;width:425px;font-size:14.5px;line-height:21.5px;color:#333}
.product .btn{left:637px;top:518px;width:190px;height:59px}

/* science */
.science{top:2171px;height:606px;background:linear-gradient(90deg,#efefef 0%,#f2f2f2 42%,#e6d9bf 62%,#d9b04e 78%,#ece7df 100%)}
.science h2{position:absolute;left:130px;top:130px;font-size:54px;color:#222}
.science p{position:absolute;left:130px;top:225px;width:350px;font-size:20px;line-height:27px}
.science .btn{left:130px;top:396px;width:190px;height:58px}

/* services */
.services{top:2777px;height:582px}
.services h2{color:#fff;top:60px}
.service{position:absolute;top:205px;width:300px;text-align:center;color:#fff;font-size:20.5px;line-height:25px;font-weight:500}
.service .ring{width:96px;height:96px;border-radius:50%;border:2px solid #fff;margin:0 auto 36px;display:flex;align-items:center;justify-content:center}
.divider-v{position:absolute;top:194px;width:2px;height:223px;background:rgba(255,255,255,.85)}

/* stories */
.stories{top:3359px;height:563px}
.stories h2{position:absolute;left:122px;top:150px;font-size:54px;line-height:58px;color:#222}
.nav-dots{position:absolute;left:134px;top:308px;display:flex;gap:8px}
.nav-dots span{width:32px;height:32px;border:2px solid #222;border-radius:50%;display:flex;align-items:center;justify-content:center}
.review{position:absolute;top:119px;width:356px;height:295px;background:var(--soft);border-radius:8px;padding:32px 42px}
.review .who{display:flex;gap:14px;align-items:center}
.avatar{width:44px;height:44px;border-radius:50%;background:#b59079}
.review .name{font-size:15px;color:#333}
.review .date{font-size:14px;color:#aaa}
.stars{margin:6px 0 0 0;color:var(--gold);font-size:17px;letter-spacing:1px}
.review p{margin-top:24px;font-size:14.5px;line-height:22px;font-style:italic;color:#666}

/* clients */
.clients{top:3922px;height:292px;background:#efefef}
.clients h2{top:40px}
.client{position:absolute;top:168px;display:flex;align-items:center;gap:10px}
.client i{width:40px;height:40px;background:#3a3a3a;display:block}
.client b{font-size:18px;letter-spacing:3px;font-weight:600;color:#333;line-height:16px}
.client small{display:block;font-size:9px;letter-spacing:4px;font-weight:500;margin-left:2px}

/* signup */
.signup{top:4214px;height:388px;background:linear-gradient(90deg,#a8393a 0%,#b9494a 35%,#c24345 60%,#bf3a3d 100%)}
.signup h2{position:absolute;left:0;width:1596px;text-align:center;top:104px;font-size:54px;color:#fff}
.signup .btn{left:685px;top:209px;width:228px;height:55px;background:#fff;color:var(--red)}

/* footer */
.site-footer{top:4602px;height:402px;background:#fff}
.site-footer .brand{left:126px;top:84px;font-size:54px}
.foot-note{position:absolute;left:128px;top:180px;width:330px;font-size:15px;line-height:19px;font-weight:500}
.foot-rule{position:absolute;top:97px;width:2px;height:166px;background:var(--red)}
.foot-col h4{font-size:20px;font-weight:600;letter-spacing:.5px;margin-bottom:22px}
.foot-col{position:absolute;top:90px;font-size:14.5px}
.foot-col li{list-style:none;margin-bottom:12px;font-weight:500}
.foot-col p{font-weight:500;line-height:19px;margin-bottom:18px}
.copyright{position:absolute;left:0;width:1200px;top:345px;text-align:center;font-size:15px;color:#333}
</style>
</head>
<body>

<header class="site-header">
  <div class="brand">Brovento</div>
  <nav class="nav"><span>About BROVENTO</span><span>About SCD</span><span>Healthcare Professionals</span><span>Patient Support</span><span>Keelan Sciences</span></nav>
  <div class="tab-cta">GET STARTED
    <svg class="arrow" viewBox="0 0 16 16"><circle cx="8" cy="8" r="7" fill="#fff"/><path d="M6.5 5l3 3-3 3" stroke="#b92b2e" stroke-width="1.8" fill="none"/></svg>
  </div>
</header>

<section class="hero" role="img" aria-label="Photo of a mother and daughter sharing fresh vegetables in a bright kitchen">
  <h1 class="display">Essential Nutrition<br>For Better Living</h1>
  <p>A Medical Food for the Dietary Management of Sickle Cell Disease in Pediatric and Adult Patients.</p>
  <div class="btn btn-solid">Learn More</div>
</section>

<section class="offers">
  <h2 class="section-title display" style="top:80px">What Brovento Offers</h2>

  <article class="offer-card" style="left:126px">
    <div class="offer-icon"><svg width="60" height="60" viewBox="0 0 60 60" fill="none" stroke="#fff" stroke-width="2.5"><path d="M30 52C14 44 14 22 30 10c16 12 16 34 0 42z"/><path d="M30 52V20"/><path d="M18 46c-8-6-10-16-6-24"/></svg></div>
    <h3>Made to<br>mimic nature</h3>
    <p>Brovento slow-release amino acids work more like natural proteins they're more efficiently absorbed, and may be easier on your gut.</p>
    <div class="more">Learn More <svg class="arrow" viewBox="0 0 16 16"><circle cx="8" cy="8" r="7" fill="#b92b2e"/><path d="M6.5 5l3 3-3 3" stroke="#fff" stroke-width="1.8" fill="none"/></svg></div>
  </article>

  <article class="offer-card" style="left:452px">
    <div class="offer-icon"><svg width="60" height="60" viewBox="0 0 60 60" fill="none" stroke="#fff" stroke-width="2.5"><path d="M8 30h44c0 12-10 20-22 20S8 42 8 30z"/><path d="M34 26l14-16"/><path d="M16 26c0-6 4-10 10-10"/></svg></div>
    <h3>Formula that's<br>flexible</h3>
    <p>Brovento is flavorless and can be mixed with many of your favorite foods without adding any after taste or causing bad breath.</p>
    <div class="more">Learn More <svg class="arrow" viewBox="0 0 16 16"><circle cx="8" cy="8" r="7" fill="#b92b2e"/><path d="M6.5 5l3 3-3 3" stroke="#fff" stroke-width="1.8" fill="none"/></svg></div>
  </article>

  <article class="offer-card" style="left:779px">
    <div class="offer-icon"><svg width="60" height="60" viewBox="0 0 60 60" fill="none" stroke="#fff" stroke-width="2.5"><path d="M30 12c-6-4-16 0-16 8-6 4-6 14 0 18 0 8 10 12 16 8 6 4 16 0 16-8 6-4 6-14 0-18 0-8-10-12-16-8z"/><path d="M30 12v34M22 24c4 0 6 3 6 6M38 34c-4 0-6-3-6-6"/></svg></div>
    <h3>A convenient<br>way to fuel up</h3>
    <p>Brovento comes in premeasured packets and bars you can take anywhere, to get the energy your body and brain need.</p>
    <div class="more">Learn More <svg class="arrow" viewBox="0 0 16 16"><circle cx="8" cy="8" r="7" fill="#b92b2e"/><path d="M6.5 5l3 3-3 3" stroke="#fff" stroke-width="1.8" fill="none"/></svg></div>
  </article>

  <div class="btn btn-outline" style="left:483px;top:623px;width:232px;height:59px">Get Started
    <svg class="arrow" viewBox="0 0 16 16"><circle cx="8" cy="8" r="7" fill="none" stroke="#b92b2e" stroke-width="1.6"/><path d="M6.5 5l3 3-3 3" stroke="#b92b2e" stroke-width="1.8" fill="none"/></svg></div>
</section>

<section class="product">
  <h2 class="section-title display" style="top:75px">The Brovento Product</h2>
  <p class="sub">A Medical Food for the Dietary Management of Sickle<br>Cell Disease in Pediatric and Adult Patients.</p>
  <svg class="abs" style="left:60px;top:180px" width="520" height="460" viewBox="0 0 520 460" role="img" aria-label="Product box surrounded by red blood cells">
    <ellipse cx="110" cy="140" rx="95" ry="115" fill="#d8383d" opacity=".85"/>
    <circle cx="303" cy="265" r="188" fill="var(--red-dark)"/>
    <rect x="200" y="160" width="210" height="230" rx="6" fill="#f2f0ee"/>
  </svg>
  <p class="product-copy">Each BROVENTO PACKET (5 mL net volume) contains a flavorful orange smoothie consisting of 2400mg of emulsified DHA, 400mg of EPA, and 150mg of other in-3 factory acids consisting of n-3, n-9. Brovento incorporates other GRAS ingredients: pasteurized egg yolk (Choline), water, orange oil, non-GMO canola oil, ascorbic acid, sucralose, citric acid, sodium ascorbate, menthol, xanthan gum, potassium sorbate, sodium benzoate, and beta-carotene.</p>
  <div class="btn btn-outline">Learn More
    <svg class="arrow" viewBox="0 0 16 16"><circle cx="8" cy="8" r="7" fill="none" stroke="#b92b2e" stroke-width="1.6"/><path d="M6.5 5l3 3-3 3" stroke="#b92b2e" stroke-width="1.8" fill="none"/></svg></div>
</section>

<section class="science" role="img" aria-label="Photo of a mother and young daughter baking together in yellow aprons">
  <h2 class="display">Brovento Science</h2>
  <p>Lorem ipsum dolor sit amet, conse ctetur adipiscing elit, sed do eius mod tempor incididunt ut laboret dolore magna aliquauis ipsum suspendisse ultricesida.</p>
  <div class="btn btn-outline">Lear More
    <svg class="arrow" viewBox="0 0 16 16"><circle cx="8" cy="8" r="7" fill="none" stroke="#b92b2e" stroke-width="1.6"/><path d="M6.5 5l3 3-3 3" stroke="#b92b2e" stroke-width="1.8" fill="none"/></svg></div>
</section>

<section class="services">
  <svg class="abs" style="left:0;top:0" width="1200" height="582" viewBox="0 0 1200 582"><path d="M0 0H1200V490Q600 660 0 490Z" fill="var(--red)"/></svg>
  <h2 class="section-title display">About Our Services</h2>
  <div class="service" style="left:102px"><div class="ring"><svg width="54" height="54" viewBox="0 0 54 54" fill="none" stroke="#fff" stroke-width="2"><path d="M20 8l10 6-8 14-10-6z"/><path d="M10 46h34M16 40h22"/><path d="M34 22c8 4 8 16 0 18"/></svg></div>Fat malabsorption<br>is a top contributor to<br>digestive/GI problems.</div>
  <div class="divider-v" style="left:433px"></div>
  <div class="service" style="left:450px"><div class="ring"><svg width="56" height="56" viewBox="0 0 56 56" fill="none" stroke="#fff" stroke-width="2"><path d="M14 22l8-5 8 5v9l-8 5-8-5z"/><path d="M30 31l8-5 8 5v9l-8 5-8-5z"/><circle cx="38" cy="14" r="3"/><circle cx="46" cy="20" r="2.5"/></svg></div>GI-related health care<br>expenses exceed $135<br>billion each year. 1</div>
  <div class="divider-v" style="left:784px"></div>
  <div class="service" style="left:813px"><div class="ring"><svg width="56" height="56" viewBox="0 0 56 56" fill="none" stroke="#fff" stroke-width="2"><path d="M14 44V34c-6-6-6-18 4-24 10-5 24 0 24 14l4 8h-4v8h-8v4"/><path d="M24 20c4-3 10-1 10 4s-6 6-10 3"/></svg></div>Other treatments can<br>be complicated and<br>less effective.</div>
</section>

<section class="stories">
  <h2 class="display">Success<br>Stories</h2>
  <div class="nav-dots">
    <span><svg width="12" height="12" viewBox="0 0 12 12"><path d="M8 2L4 6l4 4" stroke="#222" stroke-width="1.8" fill="none"/></svg></span>
    <span><svg width="12" height="12" viewBox="0 0 12 12"><path d="M4 2l4 4-4 4" stroke="#222" stroke-width="1.8" fill="none"/></svg></span>
  </div>
  <article class="review" style="left:334px">
    <div class="who"><div class="avatar"></div><div><div class="name">dana morrow</div><div class="date">2023-12-18</div></div></div>
    <div class="stars">★★★★★</div>
    <p>Lorem ipsum dolor sit amet, conse ctetur adipiscing elit, sed do eius mod tempor inc ididunt ut laboret dolore magna aliqua. Quis ipsum suspendisse ultrices gravdasus commodo viverra.</p>
  </article>
  <article class="review" style="left:711px">
    <div class="who"><div class="avatar"></div><div><div class="name">dana morrow</div><div class="date">2023-12-18</div></div></div>
    <div class="stars">★★★★★</div>
    <p>Lorem ipsum dolor sit amet, conse ctetur adipiscing elit, sed do eius mod tempor inc ididunt ut laboret dolore magna aliqua. Quis ipsum suspendisse ultrices gravdasus commodo viverra.</p>
  </article>
</section>

<section class="clients">
  <h2 class="section-title display">Client Logos</h2>
  <div class="client" style="left:218px"><i></i><b>LOREM<small>IPSUM</small></b></div>
  <div class="client" style="left:450px"><i></i><b>LOREM<small>IPSUM</small></b></div>
  <div class="client" style="left:650px"><i></i><b>LOREM<small>IPSUM</small></b></div>
  <div class="client" style="left:841px"><i></i><b>LOREM<small>IPSUM</small></b></div>
</section>

<section class="signup" role="img" aria-label="Red-tinted photo of a smiling woman in a kitchen">
  <h2 class="display">Sign up for Updates</h2>
  <div class="btn">Sign Up Now
    <svg class="arrow" viewBox="0 0 16 16"><circle cx="8" cy="8" r="7" fill="none" stroke="#b92b2e" stroke-width="1.6"/><path d="M6.5 5l3 3-3 3" stroke="#b92b2e" stroke-width="1.8" fill="none"/></svg></div>
</section>

<footer class="site-footer">
  <div class="brand">Brovento</div>
  <p class="foot-note">Ask your doctor or dietitian for more information about Brovento®. Use under medical supervision.</p>
  <div class="foot-rule" style="left:528px"></div>
  <div class="foot-col" style="left:604px"><h4>LINKS</h4>
    <ul><li>About BROVENTO</li><li>About SCD</li><li>Healthcare Professionals</li><li>Patient Support</li><li>Keelan Sciences</li></ul></div>
  <div class="foot-rule" style="left:839px"></div>
  <div class="foot-col" style="left:916px"><h4>CONTACT</h4>
    <p>Phone:<br>55501 20304050</p><p>Email:<br>info@broventomail.com</p></div>
  <div class="copyright">© 2025 All Rights are Reserved.</div>
</footer>

</body>
</html>
```